A small electrical company designed a vehicle wrap for the Corvan Haulmark 360

We designed a vehicle wrap for a small Los Angeles electrical company specializing in electrical repairs, air conditioning repair and installation, electric vehicle charging station installation, and electrical upgrades. Our clientele primarily serves residential and commercial customers. To stay within our budget, we chose a clear, eye-catching electrical and air conditioning logo that combined fonts and graphics to create a memorable impression.
Target Market(s)
electrical repair & installation, cooling&heating ,EV charger installation
Industry/Entity Type
electrical and Air conditioning
Requirements
Must have
- phone number:(555)4820173 Lic#:2048736 website www.quorvelectric.example
Nice to have
- my vehicle is Corvan haulmark 360 high roof 148'WB cargo van

```html
<!DOCTYPE html>
<html lang="en">
<head>
<meta charset="utf-8">
<title>Quorv Electric Solution Inc — Corvan Haulmark 360 Wrap</title>
<link href="https://fonts.googleapis.com/css2?family=Oswald:wght@600&family=Roboto:wght@500&family=Tinos:ital@1&display=swap" rel="stylesheet">
<style>
  :root {
    --navy: #1f2a44;
    --orange: #e8931f;
    --white: #ffffff;
    --glass: #c9ced6;
    --backdrop: #eceef1;
  }
  html, body {
    margin: 0;
    width: 1200px;
    height: 1185px;
    overflow: hidden;
    background: var(--backdrop);
  }
  .wrap-sheet { display: block; width: 1200px; height: 1185px; }
  .body-panel { fill: var(--white); stroke: #d3d6dc; stroke-width: 2; }
  .glass { fill: var(--glass); }
  .lower-band { fill: var(--navy); }
  .accent { fill: var(--orange); }
  .brand-name { font-family: "Oswald", "Arial Narrow", sans-serif; font-weight: 600; fill: var(--navy); }
  .tagline { font-family: "Tinos", "Times New Roman", serif; font-style: italic; fill: var(--orange); }
  .tag-rule { stroke: var(--orange); stroke-width: 2.5; }
  .audience-pill { fill: var(--navy); }
  .audience-text { font-family: "Roboto", Arial, sans-serif; font-weight: 500; fill: var(--orange); }
  .service { font-family: "Roboto", Arial, sans-serif; font-weight: 500; fill: var(--white); }
  .contact { font-family: "Roboto", Arial, sans-serif; font-weight: 500; fill: var(--white); }
  .licence { font-family: "Roboto", Arial, sans-serif; font-weight: 500; fill: var(--navy); }
</style>
</head>
<body>
<svg class="wrap-sheet" viewBox="0 0 1500 1481" xmlns="http://www.w3.org/2000/svg" aria-label="Vehicle wrap layout, driver and passenger sides">
  <defs>
    <g id="van-side">
      <path class="body-panel" d="M80 590 L88 480 Q120 430 200 395 L330 245 Q400 150 540 130 L1340 110 Q1378 115 1385 150 L1410 360 L1420 580 L1140 580 A95 95 0 0 0 945 580 L360 580 A95 95 0 0 0 170 580 Z"/>
      <path class="glass" d="M300 390 L400 255 Q430 240 505 240 L505 388 Z"/>
      <path class="lower-band" d="M80 500 L500 500 L545 380 L1385 378 L1415 480 L1420 580 L1140 580 A95 95 0 0 0 945 580 L360 580 A95 95 0 0 0 170 580 L80 590 Z"/>
      <path class="accent" d="M545 367 L1385 362 L1388 378 L552 382 L515 432 L578 432 L497 500 L540 445 L505 445 Z"/>
      <path class="accent" d="M370 555 L460 555 L445 575 L370 575 Z"/>
    </g>
    <path id="bolt" d="M8 0 L2 11 L7 11 L0 24 L13 8 L8 8 L12 0 Z"/>
  </defs>

  <!-- Driver side -->
  <g class="side driver-side">
    <use href="#van-side"/>
    <rect class="accent" x="690" y="215" width="120" height="120"/>
    <text class="brand-name" x="880" y="270" font-size="58" textLength="425" lengthAdjust="spacingAndGlyphs">QUORV ELECTRIC SOLUTION INC</text>
    <line class="tag-rule" x1="880" y1="297" x2="940" y2="297"/>
    <text class="tagline" x="1088" y="304" font-size="30" text-anchor="middle">we power your homes</text>
    <line class="tag-rule" x1="1236" y1="297" x2="1296" y2="297"/>
    <rect class="audience-pill" x="900" y="323" width="358" height="26" rx="13"/>
    <text class="audience-text" x="1079" y="342" font-size="17" text-anchor="middle">Residential And Commercial Customers</text>
    <use class="accent" href="#bolt" x="648" y="397"/>
    <text class="service" x="670" y="413" font-size="21">Electrical Repair &amp;Installation</text>
    <use class="accent" href="#bolt" x="648" y="428"/>
    <text class="service" x="670" y="444" font-size="21">Cooling &amp; Heating</text>
    <use class="accent" href="#bolt" x="648" y="459"/>
    <text class="service" x="670" y="475" font-size="21">EV Charger Installation</text>
    <text class="contact" x="1210" y="428" font-size="38" text-anchor="middle">(555)-482-0173</text>
    <text class="contact" x="1213" y="460" font-size="30" text-anchor="middle">quorvelectric.example</text>
    <text class="licence" x="233" y="444" font-size="23">Lic#: 2048736</text>
  </g>

  <!-- Passenger side -->
  <g class="side passenger-side">
    <g transform="translate(1500 718) scale(-1 1)">
      <use href="#van-side"/>
    </g>
    <rect class="accent" x="215" y="930" width="120" height="120"/>
    <text class="brand-name" x="418" y="985" font-size="58" textLength="430" lengthAdjust="spacingAndGlyphs">QUORV ELECTRIC SOLUTION INC</text>
    <line class="tag-rule" x1="418" y1="1014" x2="478" y2="1014"/>
    <text class="tagline" x="628" y="1021" font-size="30" text-anchor="middle">we power your homes</text>
    <line class="tag-rule" x1="778" y1="1014" x2="838" y2="1014"/>
    <rect class="audience-pill" x="437" y="1039" width="364" height="26" rx="13"/>
    <text class="audience-text" x="619" y="1058" font-size="17" text-anchor="middle">Residential And Commercial Customers</text>
    <use class="accent" href="#bolt" x="521" y="1117"/>
    <text class="service" x="543" y="1133" font-size="21">Electrical Repair &amp;Installation</text>
    <use class="accent" href="#bolt" x="521" y="1148"/>
    <text class="service" x="543" y="1164" font-size="21">Cooling &amp; Heating</text>
    <use class="accent" href="#bolt" x="521" y="1179"/>
    <text class="service" x="543" y="1195" font-size="21">EV Charger Installation</text>
    <text class="contact" x="272" y="1149" font-size="38" text-anchor="middle">(555)-482-0173</text>
    <text class="contact" x="275" y="1181" font-size="30" text-anchor="middle">quorvelectric.example</text>
    <text class="licence" x="1140" y="1165" font-size="23">Lic#: 2048736</text>
  </g>
</svg>
</body>
</html>
```